Copper Kite Pastimes- Retailer

Need to describe what Copper Kite Pastimes is, what products we carry with photos and descriptions, as well as pricing for each. shopping cart, purchase items by way of Zellpay and CoinDrift

Industry/Entity Type

Hobby / Entertainment

Coding

Coded - Design and coding required

Number of Pages Required

5+ page

Font styles to use
Sans Serif

Colors
0054AA
0677BA
7BADD7
CADEEF
E8F1F8
F0912C
F2A743
F7CA91
FBE8D2
FDF5EE
EE7325
F08F49
F5BC92
FAE3D3
FDF4ED

Requirements
Must have
• Product pages, shopping cart, checkout
Nice to have
• Video/gif, of working train or slot car tracks
Should not have
• Cartoon characters or images

```html
<!DOCTYPE html>
<html lang="en">
<head>
<meta charset="utf-8">
<title>Copper Kite Pastimes</title>
<link rel="stylesheet" href="https://fonts.googleapis.com/css2?family=Plus+Jakarta+Sans:wght@400;500;600;700;800&display=swap">
<style>
:root{
  --blue:#0054AA;--blue-2:#0677BA;--blue-soft:#E8F1F8;
  --orange:#EE7325;--orange-2:#F0912C;--orange-3:#F2A743;
  --ink:#1b1b1b;--muted:#555;--line:#e2e2e2;--band:#efefef;
  --navy:#0c1a2e;--green:#2e8b57;--star:#f0912c;
}
*{box-sizing:border-box;margin:0;padding:0}
html,body{width:1200px;height:3062px;overflow:hidden}
body{font-family:"Plus Jakarta Sans",Arial,sans-serif;color:var(--ink);background:#fff;position:relative}
a{color:inherit;text-decoration:none}
.promo{height:42px;background:var(--orange-2);color:#fff;font-size:10px;font-weight:700;display:flex;align-items:center;justify-content:center;letter-spacing:.02em}
.hero{position:relative;height:695px;background:linear-gradient(100deg,#1c1e1b 0%,#2b2c24 35%,#3e2a26 60%,#5a1f26 75%,#2a2a2a 100%);color:#fff}
.hero-photo{position:absolute;inset:0}
.nav{position:absolute;top:0;left:0;right:0;height:95px;background:rgba(20,20,20,.55);display:flex;align-items:center;padding:0 116px}
.brand{font-size:13px;font-weight:700;letter-spacing:.08em;line-height:1.2;display:flex;align-items:center;gap:8px;width:150px}
.brand-mark{width:12px;height:12px;background:var(--orange-2);border-radius:50%;flex:0 0 12px}
.nav-links{display:flex;gap:38px;margin-left:28px;font-size:12px;font-weight:700}
.nav-icons{margin-left:auto;display:flex;gap:22px}
.hero-copy{position:absolute;left:116px;top:220px;width:680px}
.hero h1{font-size:40px;font-weight:800;line-height:61px;white-space:nowrap}
.hero h1 .accent{color:var(--orange-2)}
.hero p{font-size:13.5px;line-height:22px;color:#ddd;margin-top:14px;width:500px}
.btn-outline{display:inline-flex;align-items:center;justify-content:center;border:2px solid #fff;color:#fff;font-weight:700;font-size:15px;height:70px;width:230px;margin-top:32px}
.features{height:109px;background:var(--band);display:flex;padding:30px 116px 0}
.feature{width:248px;display:flex;gap:14px}
.feature h4{font-size:10px;font-weight:800;margin-bottom:8px}
.feature p{font-size:8.5px;line-height:14px;font-weight:500;color:#333}
.section-title{font-size:28px;font-weight:800;text-align:center}
.category{padding-top:80px}
.tabs{display:flex;justify-content:center;gap:52px;margin-top:34px;font-size:13.5px;color:#555}
.tabs .active{color:var(--ink);font-weight:800;border-bottom:2px solid var(--ink);padding-bottom:4px}
.cat-grid{display:flex;gap:6px;margin:30px 116px 0}
.cat-card{width:318px;height:266px;background:#eeeeee;padding:18px 26px}
.cat-img{height:150px;background:radial-gradient(ellipse at center,#d9d9d9,#ececec 70%)}
.cat-meta{display:flex;justify-content:space-between;margin-top:42px;font-size:14px;font-weight:600}
.cat-meta b{font-size:17px}
.cat-sku{font-size:12px;color:#666;margin-top:8px}
.btn-blue{display:flex;align-items:center;justify-content:center;gap:10px;width:164px;height:70px;margin:33px auto 0;background:var(--blue);color:#fff;font-weight:700;font-size:13px}
.featured{padding:80px 0 0 116px}
.featured-head{display:flex;justify-content:space-between;padding-right:116px;align-items:center}
.featured-head h2{font-size:20px;font-weight:800}
.featured-head a{color:var(--blue);font-weight:700;font-size:15px}
.prod-row{display:flex;gap:27px;margin-top:42px;width:1200px}
.prod{flex:0 0 265px;height:505px;background:#fff;box-shadow:0 2px 12px rgba(0,0,0,.08);padding:22px 20px;position:relative}
.tag{display:inline-block;background:var(--green);color:#fff;font-size:11px;font-weight:800;padding:4px 10px}
.prod-img{height:150px;margin-top:8px;background:radial-gradient(ellipse at center,#dadada,#fff 72%)}
.prod h3{font-size:18px;font-weight:700;margin-top:16px}
.prod .desc{font-size:12.5px;line-height:20px;color:#555;margin-top:10px}
.stars{color:var(--star);font-size:14px;margin-top:6px;letter-spacing:2px}
.stars span{color:#bbb}
.price{font-size:23px;font-weight:800;margin-top:6px}
.scale{font-size:11px;color:#555;margin-top:12px}
.btn-cart{display:flex;align-items:center;justify-content:center;height:53px;border:2px solid var(--blue);color:var(--blue);font-weight:700;font-size:13px;margin-top:22px}
.brands{padding-top:78px;text-align:center}
.brands p{font-size:10.5px;color:#555;line-height:19px;margin-top:14px}
.brand-row{display:flex;justify-content:space-between;align-items:center;margin:28px 116px 0 124px;font-size:30px;font-weight:800;color:#777}
.memories{position:absolute;top:2400px;left:0;width:1200px;height:392px;background:linear-gradient(180deg,#2a2c2e,#1d1f21);color:#fff;text-align:center;padding-top:82px}
.memories .kicker{font-size:16px;font-weight:500}
.memories h2{font-size:29px;font-weight:800;margin-top:8px}
.memories p{font-size:11.5px;line-height:21px;color:#ccc;width:510px;margin:20px auto 0}
.memories .btn-outline{width:276px;margin-top:32px}
.footer{position:absolute;top:2792px;left:0;width:1200px;height:270px;background:var(--navy);color:#fff;padding:30px 52px 0}
.foot-cols{display:flex}
.foot-brand{width:285px}
.foot-brand .brand{width:auto;font-size:17px}
.foot-brand p{font-size:12px;line-height:24px;color:#ccd;margin-top:14px}
.socials{display:flex;gap:20px;margin-top:12px}
.socials span{width:26px;height:26px;border-radius:50%;background:#fff}
.col h5{font-size:12.5px;font-weight:800;margin-bottom:14px}
.col li{list-style:none;font-size:12px;color:#ccd;margin-bottom:13px;display:flex;gap:10px;align-items:center}
.col-quick{width:180px}.col-service{width:187px}.col-contact{width:240px;border-right:1px solid #2a3a55}
.col-pay{padding-left:22px}
.pay{display:flex;gap:12px}
.pay span{width:78px;height:42px;background:#fff;color:var(--blue);border-radius:4px;font-size:12px;font-weight:800;display:flex;align-items:center;justify-content:center}
.col-pay p{font-size:12px;line-height:26px;color:#ccd;margin-top:14px}
.copy{position:absolute;bottom:10px;left:0;right:0;border-top:1px solid #2a3a55;padding-top:12px;text-align:center;font-size:12px;color:#aab}
</style>
</head>
<body>
<div class="promo">"SCREEN TIME DOWN. ONE KID AT A TIME."</div>
<header class="hero">
  <div class="hero-photo" role="img" aria-label="Red semi truck parked among autumn trees"></div>
  <nav class="nav">
    <div class="brand"><span class="brand-mark"></span>COPPER KITE<br>PASTIMES</div>
    <div class="nav-links"><a>SHOP BY CATEGORY</a><a>BRANDS</a><a>COLLATOR CLUB</a><a>NEW RELEASES</a><a>ABOUT US</a></div>
    <div class="nav-icons">
      <svg width="20" height="20" viewBox="0 0 20 20" fill="none" stroke="#fff" stroke-width="1.6"><circle cx="9" cy="9" r="6.5"/><path d="M14 14l4 4"/></svg>
      <svg width="20" height="20" viewBox="0 0 20 20" fill="none" stroke="#fff" stroke-width="1.6"><circle cx="10" cy="10" r="8"/><circle cx="10" cy="8" r="3"/><path d="M4.5 15.5c3-3 8-3 11 0"/></svg>
      <svg width="20" height="20" viewBox="0 0 20 20" fill="none" stroke="#fff" stroke-width="1.6"><path d="M4 7h12l-1 11H5z"/><path d="M7 7V5a3 3 0 016 0v2"/><circle cx="17" cy="2.5" r="2" fill="#e33" stroke="none"/></svg>
    </div>
  </nav>
  <div class="hero-copy">
    <h1>PREMIUM MODELS.<br>REAL DETAIL.<br><span class="accent">BUILT FOR COLLECTORS.</span></h1>
    <p>Discover premium diecast trucks, trailers, buses, construction equipment, and collectible models from the world's most trusted brands. Built for enthusiasts, collectors, and hobbyists of every age.</p>
    <a class="btn-outline">SHOP NEW ARRIVALS</a>
  </div>
</header>
<section class="features">
  <div class="feature"><svg width="30" height="30" viewBox="0 0 30 30" fill="none" stroke="#333" stroke-width="1.4"><path d="M6 10h18l-9 13z"/><path d="M6 10l4-5h10l4 5"/></svg><div><h4>PREMIUM QUALITY</h4><p>AUTHENTIC LICENSED REPLICAS WITH<br>EXCEPTIONAL CRAFTSMANSHIP.</p></div></div>
  <div class="feature"><svg width="30" height="30" viewBox="0 0 30 30" fill="none" stroke="#333" stroke-width="1.4"><circle cx="15" cy="10" r="4"/><circle cx="7" cy="13" r="3"/><circle cx="23" cy="13" r="3"/><path d="M8 24c0-5 14-5 14 0"/></svg><div><h4>PREMIUM QUALITY</h4><p>AUTHENTIC LICENSED REPLICAS WITH<br>EXCEPTIONAL CRAFTSMANSHIP.</p></div></div>
  <div class="feature"><svg width="30" height="30" viewBox="0 0 30 30" fill="none" stroke="#333" stroke-width="1.4"><rect x="3" y="7" width="15" height="13"/><path d="M18 11h5l4 5v4h-9"/><circle cx="9" cy="22" r="2.5"/><circle cx="22" cy="22" r="2.5"/></svg><div><h4>PREMIUM QUALITY</h4><p>AUTHENTIC LICENSED REPLICAS WITH<br>EXCEPTIONAL CRAFTSMANSHIP.</p></div></div>
  <div class="feature"><svg width="30" height="30" viewBox="0 0 30 30" fill="none" stroke="#333" stroke-width="1.4"><rect x="5" y="13" width="20" height="13" rx="3"/><path d="M9 13V9a6 6 0 0112 0v4"/><path d="M15 18v3"/></svg><div><h4>PREMIUM QUALITY</h4><p>AUTHENTIC LICENSED REPLICAS WITH<br>EXCEPTIONAL CRAFTSMANSHIP.</p></div></div>
</section>
<section class="category">
  <h2 class="section-title">SHOP BY CATEGORY</h2>
  <div class="tabs"><span class="active">ALL</span><span>TRUCKS</span><span>TRAILERS</span><span>BUSES</span><span>SCALES</span><span>TOYS</span></div>
  <div class="cat-grid">
    <div class="cat-card"><div class="cat-img" role="img" aria-label="White and grey refuse truck model"></div><div class="cat-meta"><span>ORCHID RIDGELINE</span><b>$148.52</b></div><div class="cat-sku">60-8544</div></div>
    <div class="cat-card"><div class="cat-img" role="img" aria-label="White day cab truck model"></div><div class="cat-meta"><span>HARLOW H4420</span><b>$149.05</b></div><div class="cat-sku">60-8544</div></div>
    <div class="cat-card"><div class="cat-img" role="img" aria-label="Red truck model with crane bed"></div><div class="cat-meta"><span>RIDGELINE 512 DAY _7</span><b>$130.52</b></div><div class="cat-sku">60-8544</div></div>
  </div>
  <a class="btn-blue">EXPLORE <svg width="16" height="12" viewBox="0 0 16 12" fill="none" stroke="#fff" stroke-width="1.6"><path d="M1 6h13M9 1l5 5-5 5"/></svg></a>
</section>
<section class="featured">
  <div class="featured-head"><h2>FEATURED PRODUCTS</h2><a>View All Products</a></div>
  <div class="prod-row">
    <article class="prod"><span class="tag">NEW</span><div class="prod-img" role="img" aria-label="Red truck with silver tank trailer model"></div><h3>60-2353</h3><p class="desc">WHITE/BLUE HARLOW H700X WITH 60" AEROLITE SLEEPER &amp; GLACIER TANK TRAILER</p><div class="stars">★★★★<span>★</span></div><div class="price">$149.95</div><div class="scale">1/64 SCALE</div><a class="btn-cart">ADD TO CART</a></article>
    <article class="prod"><span class="tag">NEW</span><div class="prod-img" role="img" aria-label="White day cab truck model"></div><h3>60-2353</h3><p class="desc">WHITE/BLUE HARLOW H700X WITH 60" AEROLITE SLEEPER &amp; GLACIER TANK TRAILER</p><div class="stars">★★★★<span>★</span></div><div class="price">$149.95</div><div class="scale">1/64 SCALE</div><a class="btn-cart">ADD TO CART</a></article>
    <article class="prod"><span class="tag">NEW</span><div class="prod-img" role="img" aria-label="White and grey refuse truck model"></div><h3>60-2353</h3><p class="desc">WHITE/BLUE HARLOW H700X WITH 60" AEROLITE SLEEPER &amp; GLACIER TANK TRAILER</p><div class="stars">★★★★<span>★</span></div><div class="price">$149.95</div><div class="scale">1/64 SCALE</div><a class="btn-cart">ADD TO CART</a></article>
    <article class="prod"><span class="tag">NEW</span><div class="prod-img" role="img" aria-label="Red truck model with crane bed"></div><h3>60-2353</h3><p class="desc">WHITE/BLUE HARLOW H700X WITH 60" AEROLITE SLEEPER &amp; GLACIER TANK TRAILER</p><div class="stars">★★★★<span>★</span></div><div class="price">$149.95</div><div class="scale">1/64 SCALE</div><a class="btn-cart">ADD TO CART</a></article>
  </div>
</section>
<section class="brands">
  <h2 class="section-title">TOP BRANDS</h2>
  <p>FEATURING THE INDUSTRY'S LEADING NAMES IN<br>DIECAST MODELS AND COLLECTIBLES.</p>
  <div class="brand-row"><span>VANTOR</span><span>Fairway</span><span>Brightmoor</span><span>KLT</span><span>Ashvale</span><span>Roadcrest</span></div>
</section>
<section class="memories" role="img" aria-label="Dark photo of a semi truck with trailer in a parking lot">
  <div class="kicker">MORE THAN JUST MODELS.</div>
  <h2>IT'S ABOUT MEMORIES.</h2>
  <p>WHETHER YOU'RE BUILDING YOUR FIRST COLLECTION OR EXPANDING A LIFELONG PASSION, EVERY MODEL TELLS A STORY. EXPLORE PREMIUM DIECAST VEHICLES, SLOT CARS, AND COLLECTIBLES CRAFTED FOR ENTHUSIASTS OF EVERY GENERATION.</p>
  <a class="btn-outline">EXPLORE OUR COLLECTION</a>
</section>
<footer class="footer">
  <div class="foot-cols">
    <div class="foot-brand">
      <div class="brand"><span class="brand-mark"></span>COPPER KITE PASTIMES</div>
      <p>Premium scale models, trucks, trailers, buses, and toys for collectors and hobbyists.</p>
      <div class="socials"><span></span><span></span><span></span><span></span></div>
    </div>
    <div class="col col-quick"><h5>QUICK LINKS</h5><ul><li>Shop</li><li>New Releases</li><li>Collector Club</li><li>Gift Cards</li><li>Contact Us</li></ul></div>
    <div class="col col-service"><h5>CUSTOMER SERVICE</h5><ul><li>Shipping &amp; Returns</li><li>FAQ</li><li>Terms &amp; Conditions</li><li>Privacy Policy</li></ul></div>
    <div class="col col-contact"><h5>CONTACT US</h5><ul>
      <li><svg width="14" height="14" viewBox="0 0 14 14" fill="none" stroke="#fff" stroke-width="1.2"><path d="M2 1.5h3l1 3-1.5 1a8 8 0 004 4l1-1.5 3 1v3c-6 .5-11-4.5-10.5-10.5z"/></svg>555-014-2291</li>
      <li><svg width="14" height="14" viewBox="0 0 14 14" fill="none" stroke="#fff" stroke-width="1.2"><rect x="1" y="3" width="12" height="8"/><path d="M1 3l6 5 6-5"/></svg>hello@copperkitepastimes.example</li>
      <li><svg width="14" height="14" viewBox="0 0 14 14" fill="none" stroke="#fff" stroke-width="1.2"><circle cx="7" cy="7" r="6"/><path d="M1 7h12M7 1c3 3 3 9 0 12M7 1c-3 3-3 9 0 12"/></svg>www.copperkitepastimes.example</li>
      <li><svg width="14" height="14" viewBox="0 0 14 14" fill="none" stroke="#fff" stroke-width="1.2"><path d="M7 13s-4.5-4.5-4.5-7.5a4.5 4.5 0 019 0C11.5 8.5 7 13 7 13z"/><circle cx="7" cy="5.5" r="1.5"/></svg>Birchfield, MI</li>
    </ul></div>
    <div class="col col-pay"><h5>PAYMENT METHODS</h5><div class="pay"><span>CoinDrift</span><span>Zellpay</span></div><p>We accept CoinDrift &amp; Zellpay<br>for a secure checkout.</p></div>
  </div>
  <div class="copy">© 2024 Copper Kite Pastimes. All Rights Reserved.</div>
</footer>
</body>
</html>
```